Coastal Harbour and Fabrication Solutions Ltd. trading as CHFS needs a pillow pack design.

We need a pillow package design which will contain disposable protective masks. (10 to 20) per package. Front and back should have information. The back solid white (translucent). If front is solid it can have a transparent window that allows some of the mask to be seen through it.
Use the colours from the logo included in the uploaded files. Two of the colours plus white will be enough. The design layout can be horizontal or vertical as shown in the examples of uploaded files. The width of the film on which the design is to be printed is 350mm wide. Work within that parameter to create a size that is attractive. See attached examples but they seemed to have been designed for 1 mask per bag.
I would really like to see what could come out of the image with the tree silhouetted faces but obviously the colours need to change to tints of blues or blue-greens or a mixture of both.

Place the logo in the top left hand corner. You can change the black text (CHFS) in the Logo to yellow . Leave a place for the bar code somewhere at the bottom . We are in the process of ordering this now.

Method of use of masks can be illustrated but use the text from the photographed images uploaded.
The additional information that is uploaded should be on the package.

The final design should communicate "optimizing safety, maximizing comfort."

```html
<!DOCTYPE html>
<html lang="en">
<head>
<meta charset="utf-8">
<title>CHFS Disposable Protective Face Masks – Pillow Pack</title>
<link href="https://fonts.googleapis.com/css2?family=Montserrat:wght@400;500;700;800&family=Dancing+Script:wght@400&family=Great+Vibes&display=swap" rel="stylesheet">
<style>
  :root{
    --stage:#6b7f98;
    --pack-blue:#3a8bbf;
    --hero-top:#3b90c6;
    --hero-bottom:#2a6a98;
    --navy:#1b3a8c;
    --ink-blue:#1e4a90;
    --yellow:#f4ef86;
    --logo-yellow:#f3e64a;
    --white:#ffffff;
    --mask-blue:#8ccdf0;
    --swatch-purple:#7b4fc4;
    --swatch-red:#cc3b5c;
    --swatch-olive:#a49a45;
    --sans:"Montserrat",sans-serif;
    --script:"Dancing Script",cursive;
    --flourish:"Great Vibes",cursive;
  }
  *{box-sizing:border-box;margin:0;padding:0}
  html,body{width:1200px;height:759px;overflow:hidden;background:var(--stage);font-family:var(--sans)}
  .pack{position:absolute;top:114px;width:484px;height:521px;background:var(--pack-blue);overflow:hidden}
  .pack--blue{left:92px}
  .pack--white{left:627px}
  .abs{position:absolute}

  /* top band */
  .method{left:24px;top:11px;color:var(--white);font-size:9px;line-height:12.6px;font-weight:400;white-space:nowrap}
  .method h3{font-size:9.4px;font-weight:400}
  .size{left:360px;top:16px;width:100px;text-align:center;color:var(--white);font-size:9px;line-height:12.4px}
  .barcode-space{left:368px;top:47px;width:83px;height:54px}
  .donning-label{left:16px;top:89px;color:var(--white);font-size:7.4px;line-height:9px;font-weight:500}
  .step{top:78px;width:33px;height:33px;border:1.2px solid var(--white);border-radius:3px;background:#cfe3ef}

  /* hero */
  .hero{left:0;top:126px;width:484px;height:171px;background:linear-gradient(var(--hero-top),var(--hero-bottom))}
  .hero-photo{left:0;top:126px;width:242px;height:269px;background:radial-gradient(ellipse at 52% 45%,#e6e9ec 0%,#f3f4f5 45%,#ffffff 80%)}
  .hero-feature{left:242px;top:126px;width:242px;height:269px;background:var(--pack-blue)}
  .brand{display:flex;align-items:center;gap:8px}
  .brand-dot{border-radius:50%;background:#dfeec4;border:2px solid var(--white)}
  .brand-name{font-weight:700;letter-spacing:.5px}
  .brand--top{left:12px;top:136px}
  .brand--top .brand-dot{width:40px;height:40px}
  .brand--top .brand-name{font-size:17px}
  .pack--blue .brand-name{color:var(--logo-yellow)}
  .pack--white .brand-name{color:var(--navy)}
  .title{left:14px;top:204px;width:240px;text-align:center}
  .title-kicker{display:block;font-size:16.5px;font-weight:400;letter-spacing:.3px;line-height:20px}
  .title-main{display:block;font-size:31px;font-weight:800;line-height:33px}
  .title-script{display:block;font-family:var(--script);font-size:21px;line-height:26px;letter-spacing:.6px}
  .pack--blue .title{color:var(--white)}
  .pack--white .title{color:var(--navy)}
  .mask-art{border-radius:40% 45% 50% 40%;background:radial-gradient(ellipse at 45% 50%,var(--mask-blue) 0%,#6fb6e2 55%,rgba(255,255,255,0) 75%)}
  .pack--blue .mask-art{left:233px;top:131px;width:205px;height:165px}
  .pack--white .mask-art{left:268px;top:141px;width:200px;height:145px}
  .quality{left:400px;top:252px;width:67px;height:33px;border:1.3px solid var(--white);border-radius:4px;color:var(--white)}
  .quality small{position:absolute;left:22px;top:3px;font-size:6.5px}
  .quality span{position:absolute;left:6px;top:5px;font-family:var(--flourish);font-size:21px;line-height:24px}

  /* info band */
  .stripe{left:0;top:297px;width:484px;height:4px;background:var(--yellow)}
  .info{left:0;top:301px;width:484px;height:94px;background:var(--white)}
  .count{left:16px;top:313px;width:63px;height:70px;border:2px solid var(--ink-blue);border-radius:4px;background:var(--white);color:var(--ink-blue);text-align:center}
  .count b{display:block;font-size:35px;font-weight:800;line-height:34px;margin-top:3px;letter-spacing:-1px}
  .count span{display:block;font-size:22px;line-height:22px;font-weight:400}
  .claim{left:88px;top:324px;color:var(--ink-blue);font-size:8.6px;line-height:10.3px;font-weight:500}
  .colours{left:89px;top:354px;color:var(--ink-blue);font-size:8.2px;font-weight:500}
  .swatches{display:flex;gap:5px;margin-top:4px}
  .swatches i{width:11px;height:11px;display:block}
  .features{text-align:right;list-style:none;white-space:nowrap}
  .pack--blue .features{right:12px;top:311px;font-size:6.9px;line-height:9.7px;color:var(--ink-blue)}
  .pack--white .features{right:13px;top:316px;font-size:6.1px;line-height:8.9px;color:var(--white)}
  .features li.cont{padding-right:6px}

  /* bottom */
  .pack--white .foot{left:0;top:395px;width:484px;height:126px;background:var(--white)}
  .notice{left:14px;top:414px;font-size:8px;line-height:12.5px;width:266px;white-space:nowrap}
  .notice h4{font-weight:700;font-size:8.4px;margin-left:8px;margin-bottom:2px}
  .notice ul{padding-left:14px}
  .pack--blue .notice{color:var(--white)}
  .pack--white .notice{color:var(--ink-blue)}
  .brand--foot{left:310px;top:411px}
  .brand--foot .brand-dot{width:34px;height:34px}
  .brand--foot .brand-name{font-size:11px;font-weight:500}
  .address{left:288px;top:458px;font-size:8.4px;line-height:11.4px;font-style:normal;white-space:nowrap}
  .pack--blue .address{color:var(--white)}
  .pack--white .address{color:var(--ink-blue)}
</style>
</head>
<body>

<section class="pack pack--blue" aria-label="Pillow pack, blue front">
  <div class="abs method">
    <h3>Method of Use</h3>
    <ol style="list-style:none">
      <li>1. Take out the mask and make sure the nose sticking is upward.</li>
      <li>2. Make sure the nose sticking fitting the nose bridge.</li>
      <li>3. Adjust to make sure it attached onto face tightly.</li>
      <li>4. Make sure the colored side is outward.</li>
    </ol>
  </div>
  <div class="abs donning-label">PROPER DONNING OF<br>EARLOOP MASK</div>
  <div class="abs step" style="left:120px" role="img" aria-label="Step 1: wash hands"></div>
  <div class="abs step" style="left:164px" role="img" aria-label="Step 2: place mask over face"></div>
  <div class="abs step" style="left:206px" role="img" aria-label="Step 3: press nose strip"></div>
  <div class="abs step" style="left:250px" role="img" aria-label="Step 4: loop over ears"></div>
  <div class="abs step" style="left:292px" role="img" aria-label="Step 5: mask fitted"></div>
  <div class="abs size">Size :<br>175mm x 95mm</div>
  <svg class="abs barcode-space" viewBox="0 0 83 54" aria-label="Barcode area">
    <path d="M14 1H1V53H14M69 1H82V53H69" fill="none" stroke="#fff" stroke-width="1.2"/>
  </svg>

  <div class="abs hero"></div>
  <div class="abs mask-art" role="img" aria-label="Illustration of a blue disposable face mask"></div>
  <div class="abs brand brand--top"><span class="brand-dot"></span><span class="brand-name">CHFS</span></div>
  <h1 class="abs title">
    <span class="title-kicker">DISPOSABLE</span>
    <span class="title-main">PROTECTIVE</span>
    <span class="title-script">Face Masks</span>
  </h1>
  <div class="abs quality"><small>High</small><span>Quality</span></div>

  <div class="abs stripe"></div>
  <div class="abs info"></div>
  <div class="abs count"><b>10</b><span>pcs.</span></div>
  <p class="abs claim">Does not contain<br>allergic material</p>
  <div class="abs colours">Available in 3 colors
    <div class="swatches"><i style="background:var(--swatch-purple)"></i><i style="background:var(--swatch-red)"></i><i style="background:var(--swatch-olive)"></i></div>
  </div>
  <ul class="abs features">
    <li>Dual Charge Electrostatic fibres for extra filtration •</li>
    <li>Improved Nose Bridge Strips for better protection •</li>
    <li>Tri-layer barrier with 3 x 25 g/m2 material •</li>
    <li>Made of non-woven fabric, non irritant. •</li>
    <li>Air permeable structure for easy breathing. •</li>
    <li>Suitable for health care professionals, patients and the general public •</li>
    <li class="cont">as a source control of COVID-19 in accordance CDC recommendations</li>
    <li class="cont">under the FDA's EUA April 2020.</li>
  </ul>

  <div class="abs notice">
    <h4>Notice:</h4>
    <ul>
      <li>Masks will expire two (2) years from date printed on package.</li>
      <li>Non reusable, destroy after one use.</li>
      <li>Do not use if package is damaged or opened or if product<br>(mask) is damaged.</li>
      <li>Not suitable for children under three (3) years old.</li>
    </ul>
  </div>
  <div class="abs brand brand--foot"><span class="brand-dot"></span><span class="brand-name">CHFS</span></div>
  <address class="abs address">No 8, Seabreeze Landing Plaza<br>Port Marlin<br>The Coral Isles</address>
</section>

<section class="pack pack--white" aria-label="Pillow pack, white front">
  <div class="abs method">
    <h3>Method of Use</h3>
    <ol style="list-style:none">
      <li>1. Take out the mask and make sure the nose sticking is upward.</li>
      <li>2. Make sure the nose sticking fitting the nose bridge.</li>
      <li>3. Adjust to make sure it attached onto face tightly.</li>
      <li>4. Make sure the colored side is outward.</li>
    </ol>
  </div>
  <div class="abs donning-label">PROPER DONNING OF<br>EARLOOP MASK</div>
  <div class="abs step" style="left:120px" role="img" aria-label="Step 1: wash hands"></div>
  <div class="abs step" style="left:164px" role="img" aria-label="Step 2: place mask over face"></div>
  <div class="abs step" style="left:206px" role="img" aria-label="Step 3: press nose strip"></div>
  <div class="abs step" style="left:250px" role="img" aria-label="Step 4: loop over ears"></div>
  <div class="abs step" style="left:292px" role="img" aria-label="Step 5: mask fitted"></div>
  <div class="abs size">Size :<br>175mm x 95mm</div>
  <svg class="abs barcode-space" viewBox="0 0 83 54" aria-label="Barcode area">
    <path d="M14 1H1V53H14M69 1H82V53H69" fill="none" stroke="#fff" stroke-width="1.2"/>
  </svg>

  <div class="abs hero-photo" role="img" aria-label="Faded photo of a man wearing a face mask"></div>
  <div class="abs hero-feature"></div>
  <div class="abs mask-art" role="img" aria-label="Illustration of a blue disposable face mask"></div>
  <div class="abs brand brand--top"><span class="brand-dot"></span><span class="brand-name">CHFS</span></div>
  <h1 class="abs title">
    <span class="title-kicker">DISPOSABLE</span>
    <span class="title-main">PROTECTIVE</span>
    <span class="title-script">Face Masks</span>
  </h1>
  <div class="abs quality"><small>High</small><span>Quality</span></div>

  <div class="abs count"><b>10</b><span>pcs.</span></div>
  <p class="abs claim">Does not contain<br>allergic material</p>
  <div class="abs colours">Available in 3 colors
    <div class="swatches"><i style="background:var(--swatch-purple)"></i><i style="background:var(--swatch-red)"></i><i style="background:var(--swatch-olive)"></i></div>
  </div>
  <ul class="abs features">
    <li>Dual Charge Electrostatic fibres for extra filtration •</li>
    <li>Improved Nose Bridge Strips for better protection •</li>
    <li>Tri-layer barrier with 3 x 25 g/m2 material •</li>
    <li>Made of non-woven fabric, non irritant. •</li>
    <li>Air permeable structure for easy breathing. •</li>
    <li>Suitable for health care professionals, patients and the general public •</li>
    <li class="cont">as a source control of COVID-19 in accordance CDC recommendations</li>
    <li class="cont">under the FDA's EUA April 2020.</li>
  </ul>

  <div class="abs foot"></div>
  <div class="abs notice">
    <h4>Notice:</h4>
    <ul>
      <li>Masks will expire two (2) years from date printed on package.</li>
      <li>Non reusable, destroy after one use.</li>
      <li>Do not use if package is damaged or opened or if product<br>(mask) is damaged.</li>
      <li>Not suitable for children under three (3) years old.</li>
    </ul>
  </div>
  <div class="abs brand brand--foot"><span class="brand-dot"></span><span class="brand-name">CHFS</span></div>
  <address class="abs address">No 8, Seabreeze Landing Plaza<br>Port Marlin<br>The Coral Isles</address>
</section>

</body>
</html>
```